Website Design

Need a professional, clean ( no clutter) and serious website designed for Commodities. As main element Energy: Oil & Gas, Coal, Biofuel and other tabs for other products such as agricultural products fresh fruits, Vegetable as well as grain: wheat, Soy Bean, rice, nuts and organic fertilizers and one whole organic section. Meat and poultry, Edible Oils, Real Estate Investments, Aviation products airplanes and engines.

New few nice pictures of refineries and anything that evokes a sense of Oil & Gas they're usually taken at night with lighting an illuminations will look good

I'm just throwing ideas and it will have to be clustered together with the appropriate category they belong: Canned products and I will get the rest later.

I'd like to make sure that the navigation in the website and the overall experience of people who visit this site is going to be superb.

I will check out your sample websites and see which ones will be a good start for the designers.

Down the road i want to be able to add sections that will require password to get in but that's probably a little bit later down the road.

Thank you all in advance and look forward to working with you. The Log you guys did magnificent. Please ask the support to let you have it. The color motives are dark blue, white and silver in the logo.
Thanks and regards,
Bilou

Target Market(s)

Commodity Traders ( not the stock market!) it's that actual tangible physical commodities.

Industry/Entity Type

It Professional

Number of Pages Required

5+ page

Requirements
Must have
• Need a professional, clean ( no clutter), elegant and serious website. Fonts to be a good match for our Logo fonts. I need the website to be scalable and can be added more pages as our need increases. this is for professionals to go this site and be able to navigate through the site without ever getting lost in it.

```html
<!DOCTYPE html>
<html lang="en">
<head>
<meta charset="utf-8">
<title>Transmeridian Resource Group</title>
<link href="https://fonts.googleapis.com/css2?family=Open+Sans:wght@400;600;700&family=Oswald:wght@500;600&display=swap" rel="stylesheet">
<style>
:root{
  --navy:#1c3567;
  --nav:#234680;
  --accent:#3a6fc4;
  --ink:#333a44;
  --muted:#7b838e;
  --line:#e3e6ea;
  --paper:#ffffff;
  --soft:#f4f5f7;
  --footer:#1b1d21;
  --footer-bar:#111215;
}
*{box-sizing:border-box;margin:0;padding:0}
html,body{width:1200px;height:2416px;overflow:hidden;background:var(--paper)}
body{font-family:"Open Sans",Arial,sans-serif;color:var(--ink);position:relative}
.abs{position:absolute}

/* header */
.topbar{left:0;top:0;width:1200px;height:168px;background:var(--paper)}
.contact-left,.contact-right{top:56px;font-size:15px;line-height:26px;color:var(--muted)}
.contact-left{left:96px}
.contact-right{left:860px}
.contact-left .lbl,.contact-right .lbl{color:var(--accent);font-weight:600;display:flex;align-items:center;gap:8px}
.brand{left:490px;top:26px;width:220px;text-align:center}
.brand-mark{width:60px;height:60px;margin:0 auto 8px;background:var(--navy);color:#fff;font-weight:700;font-size:24px;line-height:60px}
.brand-name{font-size:12px;font-weight:600;color:var(--navy);letter-spacing:1px;text-transform:uppercase}

.mainnav{left:100px;top:168px;width:1000px;height:44px;background:var(--nav);display:flex;white-space:nowrap}
.mainnav a{flex:1 1 auto;text-align:center;color:#fff;font-size:12.5px;line-height:44px;padding:0 8px;text-decoration:none}
.mainnav a.active{background:var(--accent)}
.dropdown{left:236px;top:212px;width:200px;background:var(--paper);box-shadow:0 4px 10px rgba(0,0,0,.2)}
.dropdown a{display:block;font-size:13px;color:var(--nav);padding:10px 0;text-align:center;border-bottom:1px solid var(--line);text-decoration:none}

/* hero */
.hero{left:0;top:212px;width:1200px;height:770px;background:linear-gradient(180deg,#1d2c47 0%,#3c4e6a 35%,#8a6a3c 62%,#2a3246 80%,#162236 100%)}
.hero-title{left:100px;top:400px;font-family:"Oswald",sans-serif;font-weight:600;font-size:64px;line-height:80px;color:#fff;letter-spacing:2px}
.hero-text{left:100px;top:486px;width:400px;font-size:14px;line-height:21px;color:#e9edf3}

/* welcome */
.welcome{left:100px;top:722px;width:1000px;height:256px;background:var(--paper);display:flex}
.welcome-body{width:660px;padding:22px 26px}
.welcome-kicker{font-size:26px;color:var(--navy);font-weight:600}
.welcome-name{font-size:26px;color:var(--navy);border-bottom:2px solid var(--navy);padding-bottom:8px;display:inline-block}
.welcome-body p{font-size:12.5px;line-height:20px;color:var(--muted);margin-top:14px}
.more{font-size:12px;font-weight:700;color:var(--ink);margin-top:14px;display:flex;align-items:center;gap:6px}
.welcome-photo{width:340px;height:256px;background:linear-gradient(135deg,#c9d3de,#e7ebf0 50%,#8fa1b8)}

/* services */
.section-title{left:0;width:1200px;text-align:center;font-size:46px;color:var(--navy);font-weight:400}
.section-sub{left:240px;width:720px;text-align:center;font-size:12.5px;line-height:19px;color:var(--muted)}
.grid{left:80px;top:1158px;width:1040px;display:grid;grid-template-columns:repeat(3,320px);gap:28px 40px}
.card-img{height:196px}
.card-body{background:var(--soft);padding:16px 18px;height:126px}
.card-body h3{font-size:12.5px;font-weight:700;color:var(--ink);margin-bottom:8px}
.card-body li{list-style:none;font-size:11.5px;color:var(--muted);line-height:18px}
.card-body li::before{content:"\203A";margin-right:6px;color:var(--accent)}

/* news */
.news-title{left:80px;top:1866px;font-size:24px;color:var(--muted);font-weight:400}
.news{top:1912px;width:500px;display:flex;gap:22px}
.news-img{width:250px;height:196px;flex:none}
.news h4{font-size:16px;color:var(--navy);font-weight:400;line-height:22px}
.news .date{font-size:12px;color:var(--accent);font-weight:700;margin:8px 0}
.news p{font-size:11.5px;line-height:18px;color:var(--muted)}

/* footer */
.footer{left:0;top:2150px;width:1200px;height:214px;background:var(--footer);color:#cfd3d9}
.footer h5{font-size:14px;font-weight:600;color:#fff;letter-spacing:.5px;margin-bottom:16px}
.fcol{top:28px}
.fcol p{font-size:12.5px;line-height:20px}
.social{display:flex;gap:14px}
.social span{width:42px;height:42px;border:2px solid #cfd3d9;border-radius:50%;display:block}
.signup{display:flex;margin-top:14px}
.signup span{width:190px;height:34px;background:#fff;font-size:11px;color:#999;line-height:34px;padding-left:10px}
.signup b{width:82px;height:34px;background:var(--accent);color:#fff;font-size:13px;font-weight:600;text-align:center;line-height:34px}
.legal{left:0;top:2364px;width:1200px;height:52px;background:var(--footer-bar);color:#8b9099;font-size:11.5px;line-height:52px;text-align:center}
</style>
</head>
<body>

<header class="abs topbar">
  <div class="abs contact-left">
    <div class="lbl">
      <svg width="14" height="14" viewBox="0 0 24 24"><path fill="#3a6fc4" d="M6.6 10.8a15 15 0 0 0 6.6 6.6l2.2-2.2c.3-.3.7-.4 1-.2 1.1.4 2.3.6 3.6.6.6 0 1 .4 1 1V20c0 .6-.4 1-1 1A17 17 0 0 1 3 4c0-.6.4-1 1-1h3.5c.6 0 1 .4 1 1 0 1.3.2 2.5.6 3.6.1.3 0 .7-.2 1z"/></svg>
      Call us Anytime
    </div>
    <div>+1 555 - 010 - 2438</div>
  </div>
  <div class="abs brand">
    <div class="brand-mark">TRG</div>
    <div class="brand-name">Transmeridian Resource Group</div>
  </div>
  <div class="abs contact-right">
    <div class="lbl">
      <svg width="15" height="12" viewBox="0 0 24 18"><rect x="1" y="1" width="22" height="16" fill="none" stroke="#3a6fc4" stroke-width="2"/><path d="M1 1l11 9 11-9" fill="none" stroke="#3a6fc4" stroke-width="2"/></svg>
      Email Us
    </div>
    <div>info@transmeridiangroup.example</div>
  </div>
</header>

<div class="abs hero" role="img" aria-label="Offshore oil platform lit up at night over the sea"></div>
<h1 class="abs hero-title">OIL &amp; GAS</h1>
<p class="abs hero-text">Lorem ipsum dolor sit amet, consectetur adipiscing elit, sed do eiusmod tempor incididunt ut labore et dolore magna aliqua. Ut enim ad minim veniam, quis nostrud.</p>

<nav class="abs mainnav">
  <a class="active">Home</a>
  <a>Who We Are</a>
  <a>Private Banking &amp; Asset Management</a>
  <a>Real Estate &amp; Investments</a>
  <a>Aviation</a>
  <a>Farm &amp; Agricultural Products</a>
  <a>Technology &amp; Innovation</a>
</nav>
<div class="abs dropdown">
  <a>Monetization of Instruments</a>
  <a>Leveraging Funds</a>
  <a>Project Funding</a>
  <a>Establish Your Own Bank</a>
</div>

<section class="abs welcome">
  <div class="welcome-body">
    <div class="welcome-kicker">WELCOME TO</div>
    <div class="welcome-name">Transmeridian Resource Group</div>
    <p>Lorem ipsum dolor sit amet, consectetur adipiscing elit, sed do eiusmod tempor incididunt ut labore et dolore magna aliqua. Ut enim ad minim veniam, quis nostrud exercitation ullamco laboris nisi ut aliquip ex ea commodo consequat. Duis aute irure dolor in reprehenderit in voluptate velit esse cillum dolore eu fugiat nulla pariatur. Excepteur sint occaecat cupidatat non proident, sunt in culpa qui officia deserunt mollit anim id est laborum.</p>
    <div class="more">READ MORE
      <svg width="12" height="12" viewBox="0 0 12 12"><circle cx="6" cy="6" r="5.5" fill="#333a44"/><path d="M5 3.5L7.5 6 5 8.5" stroke="#fff" stroke-width="1.4" fill="none"/></svg>
    </div>
  </div>
  <div class="welcome-photo" role="img" aria-label="Business team meeting around a table, seen from above"></div>
</section>

<h2 class="abs section-title" style="top:1030px">Our Services</h2>
<p class="abs section-sub" style="top:1098px">Lorem ipsum dolor sit amet, consectetur adipiscing elit, sed do eiusmod tempor incididunt ut labore et dolore magna aliqua. Ut enim ad minim veniam, quis nostrud exercitation ullamco laboris nisi ut aliquip ex ea commodo.</p>

<div class="abs grid">
  <article>
    <div class="card-img" role="img" aria-label="Oil refinery silhouettes at sunset" style="background:linear-gradient(180deg,#e3a24e,#b2652a 60%,#3b2a22)"></div>
    <div class="card-body"><h3>OIL &amp; GAS</h3><ul><li>Light Crude Oil (D2, JP54)</li><li>Diesel EN 590, LNG, LPG</li><li>Gasoline, Coal and Biofuel</li></ul></div>
  </article>
  <article>
    <div class="card-img" role="img" aria-label="Financial charts and documents on a desk" style="background:linear-gradient(135deg,#dfe6ee,#9fb3cb 60%,#5f7da3)"></div>
    <div class="card-body"><h3>PRIVATE BANKING &amp; ASSET MANAGEMENT</h3><ul><li>Monetization of Instruments</li><li>Leveraging Funds</li><li>Project Funding</li></ul></div>
  </article>
  <article>
    <div class="card-img" role="img" aria-label="Large residential house with a green lawn" style="background:linear-gradient(180deg,#8db8e2,#cfd9e2 45%,#6f9a4e 75%,#4d7a33)"></div>
    <div class="card-body"><h3>REAL ESTATE &amp; INVESTMENTS</h3><ul><li>Residential Properties World Wide</li><li>Commercial Properties World Wide</li><li>Development Investments</li></ul></div>
  </article>
  <article>
    <div class="card-img" role="img" aria-label="Passenger airplane taking off in a blue sky" style="background:linear-gradient(180deg,#3e7cc4,#8fb8e4 70%,#c9dcef)"></div>
    <div class="card-body"><h3>AVIATION PRODUCTS</h3><ul><li>Commercial Airliners</li><li>Private Jets</li><li>Engines &amp; Parts</li></ul></div>
  </article>
  <article>
    <div class="card-img" role="img" aria-label="Assortment of fresh fruits and vegetables" style="background:linear-gradient(135deg,#e0b84a,#d96a2c 40%,#6ea33c 75%,#3f7a2a)"></div>
    <div class="card-body"><h3>FARM AND AGRICULTURAL PRODUCTS</h3><ul><li>Fresh Produce</li><li>Meat &amp; Poultry</li><li>Vegetables, Fruits</li></ul></div>
  </article>
  <article>
    <div class="card-img" role="img" aria-label="Glowing digital network over a world view" style="background:linear-gradient(135deg,#0d2450,#1f56a8 55%,#5aa0e6)"></div>
    <div class="card-body"><h3>TECHNOLOGY &amp; INNOVATION</h3><ul><li>Computer Hardware, CPU, Memory</li><li>Electronics, Storage &amp; Data</li><li>New Innovations in Software</li></ul></div>
  </article>
</div>

<h2 class="abs news-title">Press / News</h2>
<article class="abs news" style="left:80px">
  <div class="news-img" role="img" aria-label="Cargo ship being loaded at a port" style="background:linear-gradient(180deg,#e6a866,#a2744b 55%,#394654)"></div>
  <div>
    <h4>Nulla at diam ornare, aliquam urna</h4>
    <div class="date">JULY 21, 2015</div>
    <p>Lorem ipsum dolor sit amet, aliquam erat nulla commodo. Nunc ut lacus sed nunc vestibulum pretium nec sed ligula. Suspendisse potenti, pellentesque habitant morbi tristique senectus.</p>
    <div class="more">READ MORE &rsaquo;</div>
  </div>
</article>
<article class="abs news" style="left:620px">
  <div class="news-img" role="img" aria-label="Offshore drilling rig at dusk" style="background:linear-gradient(180deg,#22364f,#596f8c 50%,#b98650 70%,#1e2a3a)"></div>
  <div>
    <h4>Nulla at diam ornare, aliquam urna</h4>
    <div class="date">JULY 21, 2015</div>
    <p>Lorem ipsum dolor sit amet, aliquam erat nulla commodo. Nunc ut lacus sed nunc vestibulum pretium nec sed ligula. Suspendisse potenti, pellentesque habitant morbi tristique senectus.</p>
    <div class="more">READ MORE &rsaquo;</div>
  </div>
</article>

<footer class="abs footer">
  <div class="abs fcol" style="left:96px">
    <h5>CONTACT US</h5>
    <p>Transmeridian Resource Group<br>Harborview, ST 00000-1212<br>info@transmeridiangroup.example</p>
    <p style="margin-top:8px">+1-555-010-7741</p>
  </div>
  <div class="abs fcol" style="left:500px">
    <h5>FOLLOW US</h5>
    <div class="social"><span></span><span></span><span></span><span></span></div>
  </div>
  <div class="abs fcol" style="left:820px">
    <h5>NEWSLETTER</h5>
    <p>Subscribe for monthly updates on<br>commodity markets and new services.</p>
    <div class="signup"><span>Enter your email address</span><b>Sign Up</b></div>
  </div>
</footer>
<div class="abs legal">2015. All Rights Reserved. Transmeridian Resource Group</div>

</body>
</html>
```